Bright Fern Painting needs a new business card. See attachments for our logo and current card as an example.
We want to utilize the same colors in the logo, and keep all the information that is currently on it. Just need an updated and modern design.
We are open to loosing the Association Logos if it means a better design.
We are also entertaining a spot for a picture of a headshot of the person listed on the card. Head shot can be finished later.

```html
<!DOCTYPE html>
<html lang="en">
<head>
<meta charset="UTF-8">
<title>Bright Fern Painting – Business Card</title>
<link href="https://fonts.googleapis.com/css2?family=Marck+Script&family=Montserrat:wght@500;600&display=swap" rel="stylesheet">
<style>
  :root {
    --backdrop: #1d2224;
    --card-light: #ecebea;
    --brand-green: #4a5a2c;
    --brand-red: #9a4a4b;
    --brand-red-soft: #c98078;
    --ink: #1b1b1b;
    --white: #ffffff;
    --photo-green: #3d4f30;
  }
  * { margin: 0; padding: 0; box-sizing: border-box; }
  html, body { width: 1200px; height: 1000px; overflow: hidden; }
  body { background: var(--backdrop); font-family: "Montserrat", sans-serif; position: relative; }

  .card { position: absolute; left: 250px; width: 697px; height: 398px; overflow: hidden; }
  .card--front { top: 90px; background: var(--card-light); }
  .card--back { top: 537px; background: var(--brand-red); }

  .brand-name {
    position: absolute; right: 22px; top: 26px;
    display: flex; align-items: center; gap: 10px;
    font-weight: 600; font-size: 25px; color: var(--brand-green);
    line-height: 1;
  }
  .brand-name .brand-square { width: 18px; height: 18px; background: var(--brand-red); }

  .person { position: absolute; left: 215px; top: 150px; width: 280px; text-align: center; }
  .person__name { font-family: "Marck Script", cursive; font-size: 44px; color: var(--brand-green); line-height: 1; }
  .person__role { font-weight: 600; font-size: 21px; color: var(--ink); margin-top: 6px; }

  .contact-band {
    position: absolute; left: 0; top: 257px; width: 100%; height: 103px;
    background: var(--brand-red);
  }
  .contact-list { position: absolute; left: 34px; top: 270px; list-style: none; }
  .contact-list li {
    display: flex; align-items: center; gap: 5px;
    color: var(--white); font-weight: 500; font-size: 19.5px; line-height: 26.5px;
  }
  .contact-list svg { width: 19px; height: 19px; flex: none; }

  .headshot {
    position: absolute; left: 498px; top: 220px; width: 159px; height: 161px;
    border-radius: 12px;
    background: radial-gradient(circle at 50% 45%, #50643d 0%, var(--photo-green) 70%);
  }

  .back-brand {
    position: absolute; left: 0; top: 160px; width: 100%; text-align: center;
    display: flex; justify-content: center; align-items: center; gap: 12px;
    font-weight: 600; font-size: 34px; color: var(--brand-red-soft); line-height: 1;
  }
  .back-brand .brand-square { width: 22px; height: 22px; background: var(--brand-red-soft); }
  .back-url {
    position: absolute; left: 0; top: 283px; width: 100%; text-align: center;
    color: var(--white); font-weight: 500; font-size: 20px;
  }
</style>
</head>
<body>

<section class="card card--front" aria-label="Business card front">
  <div class="brand-name"><span>Bright Fern Painting</span><span class="brand-square"></span></div>

  <div class="person">
    <p class="person__name">Mark Ellison</p>
    <p class="person__role">Quality Manager</p>
  </div>

  <div class="contact-band"></div>
  <ul class="contact-list">
    <li>
      <svg viewBox="0 0 20 20"><circle cx="10" cy="10" r="9.5" fill="#000"/><path d="M7 5.5l1.6 2.4-1 1.1c.7 1.4 1.7 2.4 3 3l1.1-1 2.4 1.6-.8 1.6c-3.6-.3-6.8-3.5-7-7z" fill="#fff"/></svg>
      <span>262 555 0148</span>
    </li>
    <li>
      <svg viewBox="0 0 20 20"><rect x="2" y="5" width="16" height="11" fill="#000"/><path d="M2 5l8 6 8-6" fill="none" stroke="#fff" stroke-width="1.3"/></svg>
      <span>mark@brightfernpainting.com</span>
    </li>
    <li>
      <svg viewBox="0 0 20 20" fill="none" stroke="#000" stroke-width="1.4"><circle cx="10" cy="10" r="8"/><ellipse cx="10" cy="10" rx="3.5" ry="8"/><path d="M2 10h16M3.5 6h13M3.5 14h13"/></svg>
      <span>brightfernpainting.com</span>
    </li>
  </ul>

  <div class="headshot" role="img" aria-label="Headshot photo of the card holder"></div>
</section>

<section class="card card--back" aria-label="Business card back">
  <div class="back-brand"><span>Bright Fern Painting</span><span class="brand-square"></span></div>
  <p class="back-url">www.brightfernpainting.com</p>
</section>

</body>
</html>
```